Quimby's Yard & Garden Center Business Card Update

I need an updated Business card design for my Lawn and Garden Center. We do Landscaping installs, Lawn Mowing, Snow Removal and also have a Garden Center Retail Division. I uploaded a few of our previous business cards to give an idea of what we are starting with. The main goal of this update is to simplify and modernize the business card, not all of the services that are on the previous cards has to be on the new one but I would still like to highlight our main services. There is also a sample of our logo that Can be used in the design.

Industry/Entity Type

Landscaping

Contact Information for Business Card

Morris Quimby
Morris@Quimbysyardandgarden.example
Business (555) 201-7784
Cell (555) 318-6092

Colors

Designer to choose colors to be used in the design.

Requirements
Must have
• Services Provided :
• Landscaping
• Lawn Maintenance
• Snow Removal
• Garden Center

```html
<!DOCTYPE html>
<html lang="en">
<head>
<meta charset="utf-8">
<title>Quimby's Yard &amp; Garden Center – Business Card</title>
<link rel="stylesheet" href="https://fonts.googleapis.com/css2?family=Lato:wght@400;700&display=swap">
<style>
  :root {
    --backdrop: #d9dadf;
    --forest: #2c5128;
    --forest-dark: #1f3d1d;
    --forest-light: #3a6536;
    --paper: #ffffff;
    --ink: #2a2a2a;
    --cream: #f3f3ee;
  }
  * { box-sizing: border-box; margin: 0; padding: 0; }
  html, body {
    width: 1200px; height: 800px; overflow: hidden;
    background: var(--backdrop);
    font-family: "Lato", sans-serif;
  }
  .canvas { position: relative; width: 1200px; height: 800px; }

  .card {
    position: absolute;
    left: 352px;
    width: 480px;
    height: 276px;
  }
  .card--front {
    top: 100px;
    background: linear-gradient(120deg, var(--forest-dark) 0%, var(--forest) 55%, var(--forest-light) 100%);
  }
  .card--back {
    top: 424px;
    background: var(--paper);
  }

  .brand {
    position: absolute;
    display: flex;
    align-items: center;
    gap: 10px;
    font-weight: 700;
    white-space: nowrap;
  }
  .brand__dot { border-radius: 50%; flex: none; }
  .card--front .brand {
    left: 0; right: 0; top: 92px;
    justify-content: center;
    font-size: 50px;
    color: var(--cream);
  }
  .card--front .brand__dot { width: 26px; height: 26px; background: var(--cream); }
  .card--back .brand {
    right: 26px; top: 48px;
    font-size: 32px;
    color: var(--forest);
  }
  .card--back .brand__dot { width: 18px; height: 18px; background: var(--forest); }

  .services {
    position: absolute;
    left: 0; right: 0; bottom: 16px;
    display: flex;
    justify-content: center;
    gap: 16px;
    list-style: none;
    color: var(--cream);
    font-size: 11.5px;
  }
  .services li::before {
    content: "";
    display: inline-block;
    width: 5px; height: 5px;
    border-radius: 50%;
    background: var(--cream);
    margin-right: 5px;
    vertical-align: middle;
  }

  .person { position: absolute; left: 24px; top: 120px; }
  .person__name { font-size: 19px; font-weight: 700; color: var(--forest); line-height: 1.1; }
  .person__title { font-size: 12.5px; color: var(--ink); margin-top: 3px; }

  .rule {
    position: absolute;
    left: 24px; right: 24px; top: 172px;
    height: 1px;
    background: var(--forest);
  }

  .contact {
    position: absolute;
    left: 24px; top: 182px;
    list-style: none;
    font-size: 12.5px;
    color: var(--ink);
    line-height: 16.5px;
  }
  .contact li { display: flex; align-items: center; gap: 4px; }
  .contact svg { width: 9px; height: 9px; fill: var(--forest); flex: none; }
  .contact__label { color: var(--forest); font-weight: 700; }
</style>
</head>
<body>
<main class="canvas">

  <section class="card card--front" aria-label="Card front">
    <div class="brand"><span class="brand__dot"></span>Quimby's</div>
    <ul class="services">
      <li>Landscaping</li>
      <li>Lawn Maintenance</li>
      <li>Garden Center</li>
      <li>Snow Removal</li>
    </ul>
  </section>

  <section class="card card--back" aria-label="Card back">
    <div class="brand"><span class="brand__dot"></span>Quimby's</div>

    <div class="person">
      <p class="person__name">Morris Quimby</p>
      <p class="person__title">Director</p>
    </div>

    <div class="rule"></div>

    <ul class="contact">
      <li>
        <svg viewBox="0 0 10 10" aria-hidden="true"><path d="M2 0.5 L3.6 0.5 L4.2 2.8 L3 3.6 Q4 5.8 6.2 7 L7 5.8 L9.5 6.4 L9.5 8 Q9.5 9.5 8 9.5 Q1 9 0.5 2 Q0.5 0.5 2 0.5Z"/></svg>
        (555) 201-7784 <span class="contact__label">Business</span>
      </li>
      <li>
        <svg viewBox="0 0 10 10" aria-hidden="true"><path d="M2 0.5 L3.6 0.5 L4.2 2.8 L3 3.6 Q4 5.8 6.2 7 L7 5.8 L9.5 6.4 L9.5 8 Q9.5 9.5 8 9.5 Q1 9 0.5 2 Q0.5 0.5 2 0.5Z"/></svg>
        (555) 318-6092 <span class="contact__label">Cell</span>
      </li>
      <li>
        <svg viewBox="0 0 10 10" aria-hidden="true"><path d="M0 2 H10 V8.5 H0Z M0.8 2.6 L5 5.6 L9.2 2.6" stroke="#fff" stroke-width="0.8"/></svg>
        Morris@Quimbysyardandgarden.example
      </li>
      <li>
        <svg viewBox="0 0 10 10" aria-hidden="true"><circle cx="5" cy="5" r="4.6"/><path d="M0.6 5 H9.4 M5 0.5 V9.5 M1.5 2.8 H8.5 M1.5 7.2 H8.5" stroke="#fff" stroke-width="0.6" fill="none"/><ellipse cx="5" cy="5" rx="2" ry="4.5" stroke="#fff" stroke-width="0.6" fill="none"/></svg>
        www.quimbysyardandgarden.example
      </li>
    </ul>
  </section>

</main>
</body>
</html>
```